Business Card for Dental Office

Our office is in the Hillcrest section of San Diego, California which is a well-established area. Maybe the back can be a map of our office location

```html
<!DOCTYPE html>
<html lang="en">
<head>
<meta charset="utf-8">
<title>Elmridge Dental – Business Card</title>
<link rel="stylesheet" href="https://fonts.googleapis.com/css2?family=Open+Sans:wght@400;600;700&display=swap">
<style>
  :root {
    --page: #2b2b2b;
    --card: #121212;
    --card-edge: #1c1c1c;
    --ink: #f2f2f2;
    --ink-soft: #d6d6d6;
    --rule: #3a3a3a;
  }
  * { box-sizing: border-box; margin: 0; padding: 0; }
  html, body { width: 1200px; height: 900px; overflow: hidden; }
  body {
    background: var(--page);
    font-family: "Open Sans", Arial, sans-serif;
    color: var(--ink);
    display: flex;
    align-items: center;
    justify-content: center;
    gap: 60px;
  }
  .card {
    width: 520px;
    height: 298px;
    border-radius: 22px;
    background: linear-gradient(160deg, var(--card-edge), var(--card) 60%);
    box-shadow: 0 10px 30px rgba(0,0,0,.45);
    position: relative;
    display: flex;
  }
  .brand {
    display: flex;
    align-items: center;
    gap: 10px;
    font-weight: 600;
    font-size: 26px;
    letter-spacing: .5px;
    color: var(--ink);
    white-space: nowrap;
  }
  .brand-dot {
    width: 12px; height: 12px;
    border-radius: 50%;
    background: var(--ink);
  }
  .card-front .brand-zone {
    width: 280px;
    display: flex;
    align-items: center;
    justify-content: center;
  }
  .card-front .divider {
    width: 1px;
    margin: 26px 0;
    background: var(--rule);
  }
  .contact {
    padding: 38px 0 0 26px;
    display: flex;
    flex-direction: column;
  }
  .contact-name { font-size: 18px; font-weight: 700; line-height: 1.2; }
  .contact-role { font-size: 12px; color: var(--ink-soft); margin-bottom: 18px; }
  .contact-address { font-size: 12.5px; line-height: 1.45; color: var(--ink-soft); margin-bottom: 12px; }
  .contact-list { list-style: none; font-size: 12.5px; color: var(--ink-soft); }
  .contact-list li { display: flex; align-items: center; gap: 9px; line-height: 1.6; }
  .contact-list svg { width: 11px; height: 11px; fill: var(--ink); flex: none; }
  .card-back { align-items: center; justify-content: center; }
  .card-back .brand { font-size: 30px; }
</style>
</head>
<body>
  <section class="card card-front">
    <div class="brand-zone">
      <div class="brand"><span class="brand-dot"></span>Elmridge Dental</div>
    </div>
    <div class="divider"></div>
    <div class="contact">
      <p class="contact-name">Daniel Hale</p>
      <p class="contact-role">Managing Director</p>
      <p class="contact-address">4820, Ridge Avenue Here<br>Country Name, 921030.</p>
      <ul class="contact-list">
        <li><svg viewBox="0 0 24 24"><path d="M6.6 10.8a15.1 15.1 0 0 0 6.6 6.6l2.2-2.2a1 1 0 0 1 1-.25 11.4 11.4 0 0 0 3.6.57 1 1 0 0 1 1 1V20a1 1 0 0 1-1 1A17 17 0 0 1 3 4a1 1 0 0 1 1-1h3.5a1 1 0 0 1 1 1c0 1.25.2 2.45.57 3.57a1 1 0 0 1-.25 1z"/></svg>055-210 384 116</li>
        <li><svg viewBox="0 0 24 24"><path d="M2 5h20v14H2zm2 2v.5l8 5 8-5V7l-8 5z"/></svg>hello@elmridge.com</li>
        <li><svg viewBox="0 0 24 24"><path d="M10.6 13.4a1 1 0 0 1 0-1.4l3.5-3.5a1 1 0 1 1 1.4 1.4L12 13.4a1 1 0 0 1-1.4 0zM7 11l-2.5 2.5a3.5 3.5 0 0 0 5 5L12 16l1.4 1.4-2.5 2.5a5.5 5.5 0 0 1-7.8-7.8L5.6 9.6zm10 2 2.5-2.5a3.5 3.5 0 0 0-5-5L12 8l-1.4-1.4 2.5-2.5a5.5 5.5 0 0 1 7.8 7.8l-2.5 2.5z"/></svg>www.elmridgedental.com</li>
      </ul>
    </div>
  </section>

  <section class="card card-back">
    <div class="brand"><span class="brand-dot"></span>Elmridge Dental</div>
  </section>
</body>
</html>
```